Business Card design for Brightvale Global

we need a business card design for our company. we are a trading company based in LA.

Company Name: Brightvale Global Corp.
Contact: Marla Ostrov
Title: CEO
Tel: 310-447-2093
Email: bvgcorp7@mailnest.example

Target Market(s)

International, especially China

Industry/Entity Type

Trade

Colors
3276b5
34a7d8
0555a3
0493ce
85cae6
85acd3
d0dfed
cee9f5

Requirements
Must have
• Logo and contact, to have international/global feeling

```html
<!DOCTYPE html>
<html lang="en">
<head>
<meta charset="utf-8">
<title>Brightvale Global Corp. — Business Card</title>
<link rel="stylesheet" href="https://fonts.googleapis.com/css2?family=Open+Sans:wght@400;600&display=swap">
<style>
  :root {
    --bg: #d6d6d6;
    --card: #ffffff;
    --band: #2fa6d9;
    --rule: #85cae6;
    --frame: #0493ce;
    --ink: #333a40;
    --ink-soft: #4a5058;
    --brand: #0555a3;
    --shadow: rgba(0, 0, 0, 0.18);
  }
  * { box-sizing: border-box; margin: 0; padding: 0; }
  html, body {
    width: 1200px;
    height: 1000px;
    overflow: hidden;
    background: var(--bg);
    font-family: "Open Sans", "Segoe UI", Arial, sans-serif;
  }
  .canvas {
    position: relative;
    width: 1200px;
    height: 1000px;
  }
  .card {
    position: absolute;
    width: 620px;
    height: 354px;
    background: var(--card);
    box-shadow: 0 10px 28px var(--shadow);
    overflow: hidden;
  }

  /* Front */
  .card--front { left: 110px; top: 100px; }
  .front__band {
    position: absolute;
    left: 0; top: 0;
    width: 100%;
    height: 150px;
    background: var(--band);
  }
  .front__company {
    position: absolute;
    left: 0; right: 0;
    top: 84px;
    text-align: center;
    color: #ffffff;
    font-size: 30px;
    font-weight: 400;
    letter-spacing: 0.2px;
  }
  .front__rule {
    position: absolute;
    height: 2px;
    background: var(--rule);
  }
  .front__rule--upper { left: 80px; right: 0; top: 176px; }
  .front__rule--lower { left: 0; right: 150px; top: 262px; }
  .front__person {
    position: absolute;
    left: 0; right: 0;
    top: 188px;
    text-align: center;
    padding-left: 60px;
  }
  .front__name {
    color: var(--ink);
    font-size: 22px;
    font-weight: 400;
    line-height: 1.2;
  }
  .front__title {
    color: var(--ink-soft);
    font-size: 14px;
    margin-top: 4px;
  }
  .front__contacts {
    position: absolute;
    left: 70px;
    top: 280px;
    list-style: none;
  }
  .contact {
    display: flex;
    align-items: center;
    gap: 14px;
    color: var(--ink-soft);
    font-size: 15px;
    height: 26px;
  }
  .contact__icon { width: 16px; height: 16px; flex: none; }

  /* Back */
  .card--back { left: 470px; top: 550px; }
  .back__frame {
    position: absolute;
    left: 38px; top: 38px; right: 38px; bottom: 38px;
    border: 2px solid var(--frame);
  }
  .back__brand {
    position: absolute;
    left: 0; right: 0; top: 0; bottom: 0;
    display: flex;
    align-items: center;
    justify-content: center;
    gap: 16px;
  }
  .brand__dot {
    width: 44px; height: 44px;
    border-radius: 50%;
    background: var(--brand);
  }
  .brand__name {
    color: var(--brand);
    font-size: 40px;
    font-weight: 600;
    letter-spacing: 0.3px;
  }
</style>
</head>
<body>
<main class="canvas">

  <section class="card card--front" aria-label="Business card front">
    <div class="front__band"></div>
    <h1 class="front__company">Brightvale Global Corp</h1>
    <div class="front__rule front__rule--upper"></div>
    <div class="front__person">
      <p class="front__name">Marla Ostrov</p>
      <p class="front__title">Chief Executive Officer</p>
    </div>
    <div class="front__rule front__rule--lower"></div>
    <ul class="front__contacts">
      <li class="contact">
        <svg class="contact__icon" viewBox="0 0 24 24" aria-hidden="true">
          <path fill="#3a4048" d="M6.6 10.8a15.1 15.1 0 0 0 6.6 6.6l2.2-2.2c.3-.3.7-.4 1-.2 1.1.4 2.3.6 3.6.6.6 0 1 .4 1 1V20c0 .6-.4 1-1 1A17 17 0 0 1 3 4c0-.6.4-1 1-1h3.5c.6 0 1 .4 1 1 0 1.3.2 2.5.6 3.6.1.3 0 .7-.2 1z"/>
        </svg>
        <span>310-447-2093</span>
      </li>
      <li class="contact">
        <svg class="contact__icon" viewBox="0 0 24 24" aria-hidden="true">
          <rect x="2" y="5" width="20" height="14" fill="#3a4048"/>
          <path d="M2 5l10 8 10-8" fill="none" stroke="#ffffff" stroke-width="1.5"/>
        </svg>
        <span>bvgcorp7@mailnest.example</span>
      </li>
    </ul>
  </section>

  <section class="card card--back" aria-label="Business card back">
    <div class="back__frame"></div>
    <div class="back__brand">
      <span class="brand__dot"></span>
      <span class="brand__name">Brightvale Global</span>
    </div>
  </section>

</main>
</body>
</html>
```